Hi,

I would like to have a invitation made for a party. exactly like the picture in the link below.

http://pinboardia.example/pin/730215948361027459/

However, Please change the colors into fun/ girly feeling. font can be different and size of the card should be the same

Name of the girl: RINA
What: Bachelorette Party
Where:TOLO Boat
Dubai Coral Quay Sailing Club
When:7th of February 2013

No RSVP required. (so no need to put it)

```html
<!DOCTYPE html>
<html lang="en">
<head>
<meta charset="utf-8">
<title>Rina's Bachelorette Party Invitation</title>
<link rel="stylesheet" href="https://fonts.googleapis.com/css2?family=Cinzel:wght@400;700&family=Dancing+Script:wght@400;500&family=EB+Garamond&display=swap">
<style>
  :root {
    --lilac: #b384bc;
    --white: #ffffff;
    --ink: #4a4a4a;
    --label-ink: #3a3140;
    --gold: #ece27a;
    --serif: "Cinzel", "Times New Roman", serif;
    --script: "Dancing Script", "Brush Script MT", cursive;
    --book: "EB Garamond", Georgia, serif;
  }
  * { box-sizing: border-box; margin: 0; padding: 0; }
  html, body { width: 1200px; height: 563px; overflow: hidden; background: var(--lilac); }

  .invitation {
    position: relative;
    width: 1200px;
    height: 563px;
    background: var(--lilac);
    overflow: hidden;
  }

  .trim { position: absolute; left: 0; top: 0; width: 1200px; height: 563px; }
  .trim line { stroke: var(--gold); stroke-width: 2.5; }
  .trim .flourish { fill: var(--gold); }

  .honoree {
    position: absolute;
    left: 26px;
    top: 126px;
    font-family: var(--serif);
    font-weight: 400;
    font-size: 86px;
    line-height: 1;
    letter-spacing: 4px;
    color: var(--white);
    white-space: nowrap;
  }
  .tagline {
    position: absolute;
    left: 29px;
    top: 238px;
    font-family: var(--script);
    font-weight: 500;
    font-size: 54px;
    line-height: 1;
    color: var(--white);
    white-space: nowrap;
  }
  .headline {
    position: absolute;
    left: 52px;
    top: 275px;
    font-family: var(--serif);
    font-weight: 400;
    font-size: 200px;
    line-height: 1;
    letter-spacing: 2px;
    color: var(--ink);
    white-space: nowrap;
  }

  .details-card {
    position: absolute;
    left: 833px;
    top: 40px;
    width: 347px;
    height: 487px;
    border: 10px solid var(--white);
    border-radius: 62px;
    padding-top: 36px;
    text-align: center;
  }
  .details { display: block; }
  .details dt {
    font-family: var(--serif);
    font-weight: 700;
    font-size: 18px;
    line-height: 24px;
    color: var(--label-ink);
  }
  .details dd {
    font-family: var(--script);
    font-size: 22px;
    line-height: 29px;
    color: var(--white);
  }
  .details dd + dt { margin-top: 36px; }
  .details dt.when { margin-top: 30px; }
  .details .year {
    font-family: var(--book);
    font-size: 24px;
  }
  .card-rule {
    position: absolute;
    left: 74px;
    top: 420px;
    width: 180px;
    height: 28px;
  }
  .card-rule line { stroke: var(--gold); stroke-width: 2.5; }
  .card-rule .flourish { fill: var(--gold); }
</style>
</head>
<body>
<main class="invitation">
  <svg class="trim" viewBox="0 0 1200 563" aria-hidden="true">
    <!-- top corner bracket -->
    <line x1="287" y1="16" x2="393" y2="16"/>
    <line x1="391" y1="15" x2="391" y2="100"/>
    <rect class="flourish" x="354" y="20" width="26" height="42" rx="6" role="img" aria-label="Gold scroll flourish"/>
    <!-- bottom corner bracket -->
    <line x1="19" y1="453" x2="19" y2="550"/>
    <line x1="18" y1="549" x2="127" y2="549"/>
    <rect class="flourish" x="27" y="495" width="38" height="42" rx="6" role="img" aria-label="Gold scroll flourish"/>
    <!-- divider above the tagline -->
    <line x1="473" y1="181" x2="713" y2="181"/>
    <rect class="flourish" x="562" y="158" width="62" height="20" rx="6" role="img" aria-label="Gold scroll flourish"/>
  </svg>

  <h1 class="honoree">RINA’S</h1>
  <p class="tagline">Last chance to celebrate being</p>
  <p class="headline">SINGLE</p>

  <section class="details-card">
    <dl class="details">
      <dt>WHO</dt>
      <dd>Rina</dd>
      <dt>WHAT</dt>
      <dd>Bachelorette Party</dd>
      <dt>WHERE</dt>
      <dd>Tolo Boat</dd>
      <dd>Dubai Coral Quay Sailing Club</dd>
      <dt class="when">WHEN</dt>
      <dd>7th of February</dd>
      <dd class="year">2013</dd>
    </dl>
    <svg class="card-rule" viewBox="0 0 180 28" aria-hidden="true">
      <line x1="0" y1="9" x2="180" y2="9"/>
      <rect class="flourish" x="70" y="11" width="40" height="15" rx="5" role="img" aria-label="Gold scroll flourish"/>
    </svg>
  </section>
</main>
</body>
</html>
```